Norwegian language blog www.lumadio.com / www.lumadio.no

I want to make a blog where I share my thoughts and ideas about Norwegian language. I already have a YouTube channel with almost 40000 followers and a podcast with more than 10000 listeners, so this blog will be the extention of those channels. In addition I have my own online school, check www.vilpa.noI have a logo and everything, so I just need a fresh vibrant blog to go with my concept. I want to keep the colors in my logo and also add my logo of course. Then the blog should be easy to read. I need some pictures of the Norwegian flag or something.I want a fun and cool design.
Check my youtube here: https://www.videohub.example/channel/UCxqWPT415mKaZ8Lf2dHoRwn?view_as=subscriber
Website here: www.vilpa.no

The blog will be for my new domain www.lumadio.no and I also have the same domain with www.lumadio.com - I want to put them both in one URL, like when you write www.lumadio.no or .com you will reach the same page.

Target Market(s)

Student who want to learn Norwegian and learn about Norwegian culture

Industry/Entity Type

Education

Coding

Coded - Design and coding required

Number of Pages Required

1 page

Font styles to use
Sans Serif

Colors
e34398
00a990
f78f20
0492cd
86cfc6
85cae6
f8ba93
eda3c7
ffc214

Requirements
Must have
• The colors of my logo, check www.vilpa.no
• Cool and elegant layout
• Pictures of Norway
• Picture of me
• Picture of the Norwegian flag
Should not have
• too many colors and pictures of random people

```html
<!DOCTYPE html>
<html lang="en">
<head>
<meta charset="utf-8">
<title>Lumadio Notes – Norwegian Language</title>
<link href="https://fonts.googleapis.com/css2?family=Lato:wght@400;700&display=swap" rel="stylesheet">
<style>
:root{
  --teal:#00b3a6;
  --teal-soft:#5ecfc8;
  --band:#a7dad6;
  --panel:#f3f2ef;
  --white:#ffffff;
  --ink:#2b2b2b;
  --muted:#8a8a8a;
  --line:#e2e2e2;
  --grey-head:#a3a6a9;
}
*{box-sizing:border-box;margin:0;padding:0}
html,body{width:1200px;height:1200px;overflow:hidden;background:var(--white)}
body{font-family:'Lato',sans-serif;color:var(--ink)}
.canvas{position:relative;width:1200px;height:1200px;overflow:hidden}
.stage{position:absolute;left:0;top:0;width:1500px;height:1500px;transform:scale(.8);transform-origin:0 0}
.abs{position:absolute}
.band{position:absolute;left:0;width:1500px;background:var(--band)}
.sidebar{position:absolute;left:214px;width:361px;background:var(--white);border-radius:20px 0 0 20px}
.main{position:absolute;left:575px;width:794px;background:var(--panel);border-radius:20px}
.brand{position:absolute;left:0;width:361px;top:34px;text-align:center;font-size:20px;font-weight:700;color:#6e6e6e;letter-spacing:1px}
.nav{position:absolute;left:27px;top:43px;display:flex;gap:36px;font-size:14px}
.nav .caret{font-size:9px;margin-left:8px}
.contact{position:absolute;left:647px;top:31px;width:114px;height:42px;background:var(--teal);color:#fff;font-weight:700;font-size:13px;display:flex;align-items:center;justify-content:center;gap:5px}
.rule{position:absolute;left:15px;width:765px;height:1px;background:#dcdcdc}
.search{position:absolute;left:197px;width:399px;height:38px;border:1px solid #ddd;border-radius:19px;background:#fff;font-size:13px;color:#aaa;padding:11px 14px}
.cat-row{position:absolute;left:0;width:361px;height:47px;border-top:1px solid var(--line);display:flex;align-items:center;font-size:14px}
.cat-row .ico{width:48px;display:flex;justify-content:center}
.cat-row .arrow{position:absolute;left:292px;font-size:9px}
.badge{position:absolute;left:314px;width:27px;height:27px;border-radius:50%;border:1.5px solid var(--teal);color:var(--teal);font-size:11px;display:flex;align-items:center;justify-content:center;font-weight:700}
.sub{position:absolute;left:18px;font-size:12px;color:#777;display:flex;gap:8px;align-items:center}
.tags{position:absolute;left:0;width:361px;height:57px;border:1px solid var(--line);display:flex;justify-content:center;align-items:center;gap:20px}
.tag{background:#eee;font-size:10px;color:#555;padding:4px 14px 4px 24px;position:relative}
.tag::before{content:"";position:absolute;left:8px;top:7px;width:5px;height:5px;border-radius:50%;border:1px solid #bbb;background:#fff}
.stat{position:absolute;top:257px;width:169px;height:72px;background:#fff;border-top:2px solid var(--teal);box-shadow:0 1px 2px rgba(0,0,0,.15);text-align:center;font-size:14px;padding-top:16px;line-height:22px}
.stat svg{vertical-align:-4px;margin-right:6px}
.list-item{position:absolute;left:30px;width:735px;height:41px;border-bottom:1px solid var(--line);font-size:13.5px;font-weight:700;color:#555;display:flex;align-items:center;gap:10px}
.step{position:absolute;left:10px;width:330px;height:43px;border-top:1px solid var(--line);font-size:14px;display:flex;align-items:center;padding-left:15px}
.meta{position:absolute;top:260px;height:49px;border:1px solid var(--line);font-size:14px;display:flex;align-items:center;padding-left:16px;gap:6px}
</style>
</head>
<body>
<div class="canvas">
<div class="stage">

<div class="band" style="top:0;height:756px"></div>
<div class="band" style="top:795px;height:705px"></div>

<aside class="sidebar" style="top:13px;height:735px">
  <div class="brand">Lumadio Notes</div>
  <div class="cat-row" style="top:102px;background:#f0f0f0;border-top:0"><span class="ico"><svg width="20" height="18" viewBox="0 0 20 18"><path d="M10 1 1 9h3v8h4v-5h4v5h4V9h3z" fill="#222"/></svg></span>Index</div>
  <div class="cat-row" style="top:149px"><span class="ico"><svg width="22" height="16" viewBox="0 0 22 16"><path d="M1 1h7l2 2h9v3M1 1v14h16l4-9H5L1 15" fill="none" stroke="#333" stroke-width="1.4"/></svg></span>Norwegian Language<span class="arrow">▼</span><span class="badge" style="top:10px">51</span></div>
  <div class="sub" style="top:202px;color:#222;font-weight:700"><svg width="12" height="10" viewBox="0 0 12 10"><path d="M.5.5h4l1 1h6v8H.5z" fill="none" stroke="#333"/></svg>Norwegian Words</div>
  <div class="sub" style="top:233px"><svg width="12" height="10" viewBox="0 0 12 10"><path d="M.5.5h4l1 1h6v8H.5z" fill="none" stroke="#999"/></svg>Norwegian Paragraphs</div>
  <div class="sub" style="top:264px"><svg width="12" height="10" viewBox="0 0 12 10"><path d="M.5.5h4l1 1h6v8H.5z" fill="none" stroke="#999"/></svg>Norwegian related</div>
  <div class="sub" style="top:295px"><svg width="12" height="10" viewBox="0 0 12 10"><path d="M.5.5h4l1 1h6v8H.5z" fill="none" stroke="#999"/></svg>Norwegian title</div>
  <div class="cat-row" style="top:333px"><span class="ico"><svg width="18" height="22" viewBox="0 0 18 22"><path d="M1 1h11l5 5v15H1z" fill="none" stroke="#333" stroke-width="1.3"/></svg></span>Norwegian Dictionary<span class="arrow">◀</span><span class="badge" style="top:10px">79</span></div>
  <div class="cat-row" style="top:380px"><span class="ico"><svg width="20" height="16" viewBox="0 0 20 16"><path d="M1 2h18M1 6h18M1 10h18M1 14h18" stroke="#333" stroke-width="2"/></svg></span>Language Resources<span class="arrow">◀</span><span class="badge" style="top:10px">94</span></div>
  <div class="cat-row" style="top:427px"><span class="ico"><svg width="20" height="20" viewBox="0 0 20 20"><circle cx="6" cy="6" r="4" fill="none" stroke="#333" stroke-width="1.6"/><circle cx="14" cy="14" r="4" fill="none" stroke="#333" stroke-width="1.6"/><path d="M9 9l2 2" stroke="#333" stroke-width="1.6"/></svg></span>Useful resources<span class="arrow">◀</span><span class="badge" style="top:10px">20</span></div>
  <div class="cat-row" style="top:474px"><span class="ico" style="width:55px"><svg width="18" height="18" viewBox="0 0 18 18"><path d="M9 1v16M1 9h16" stroke="#222" stroke-width="3.5"/></svg></span>Norway news<span class="badge" style="top:10px">63</span></div>
  <div class="cat-row" style="top:521px"><span class="ico" style="width:55px"><svg width="24" height="16" viewBox="0 0 24 16"><rect x="1" y="1" width="22" height="14" fill="none" stroke="#333" stroke-width="1.3"/><rect x="4" y="4" width="6" height="7" fill="none" stroke="#333"/><path d="M12 4h8M12 7h8M12 10h8" stroke="#333"/></svg></span>Norwegian Newspaper<span class="badge" style="top:10px">11</span></div>
  <div class="cat-row" style="top:568px;height:62px;border-bottom:1px solid var(--line)"></div>
  <div class="abs" style="left:17px;top:581px;width:327px;height:35px;border:1px solid #ddd;font-size:13px;color:#aaa;padding:9px 14px">Search categories...</div>
  <div class="tags" style="top:644px"><span class="tag">Norwegian</span><span class="tag">Norway</span><span class="tag">Language</span></div>
</aside>

<main class="main" style="top:13px;height:735px">
  <nav class="nav"><span>Home<span class="caret">▼</span></span><span>Articles</span><span>blog</span><span>F.A.Q</span></nav>
  <div class="contact">➤ Contact us</div>
  <div class="rule" style="top:103px"></div>
  <h1 class="abs" style="left:0;width:794px;top:122px;text-align:center;color:var(--teal);font-size:28px;font-weight:400">Norwegian Language</h1>
  <div class="search" style="top:172px">Search database...<svg style="position:absolute;right:12px;top:11px" width="14" height="14" viewBox="0 0 14 14"><circle cx="6" cy="6" r="4.5" fill="none" stroke="#777" stroke-width="1.6"/><path d="M9.5 9.5 13 13" stroke="#777" stroke-width="1.8"/></svg></div>
  <div class="stat" style="left:15px"><svg width="24" height="16" viewBox="0 0 24 16"><path d="M12 1 1 6l11 5 11-5zM5 8v5c4 3 10 3 14 0V8l-7 3z" fill="var(--teal)"/></svg>318<br>Articles</div>
  <div class="stat" style="left:213px"><svg width="22" height="16" viewBox="0 0 22 16"><path d="M1 1h7l2 2h8v3H5L1 15zM5 7h16l-4 8H1z" fill="var(--teal)"/></svg>20<br>Categories</div>
  <div class="stat" style="left:411px"><svg width="20" height="20" viewBox="0 0 20 20"><path d="M10 1l8 5v8l-8 5-8-5V6z" fill="none" stroke="var(--teal)" stroke-width="2"/><path d="M2 6l8 5 8-5M10 11v8" stroke="var(--teal)" stroke-width="2" fill="none"/></svg>61<br>Tests</div>
  <div class="stat" style="left:609px"><svg width="22" height="18" viewBox="0 0 22 18"><ellipse cx="9" cy="7" rx="8" ry="6" fill="var(--teal)"/><path d="M4 11 2 16l6-3z" fill="var(--teal)"/><ellipse cx="15" cy="11" rx="6" ry="4.5" fill="var(--teal)"/></svg>210<br>F.A.Q</div>

  <div class="abs" style="left:15px;top:357px;width:765px;height:350px;background:#fff;border:1px solid #ddd"></div>
  <div class="abs" style="left:397px;top:357px;width:383px;height:86px;background:var(--panel);border-bottom:1px solid #ddd"></div>
  <div class="abs" style="left:15px;top:372px;width:382px;text-align:center;color:#888"><div style="font-size:24px">12</div><div style="font-size:14px;margin-top:12px">Latest Articles</div></div>
  <div class="abs" style="left:397px;top:373px;width:383px;text-align:center;color:#999"><div style="font-size:24px">17</div><div style="font-size:14px;margin-top:12px">Popular Articles</div></div>
  <div class="list-item" style="top:452px"><svg width="11" height="13" viewBox="0 0 11 13"><path d="M.5.5h7l3 3v9H.5zM3 6h5M3 8h5M3 10h5" fill="none" stroke="#aaa"/></svg><span>How to start learning Norwegian language in ...</span></div>
  <div class="list-item" style="top:493px"><svg width="11" height="13" viewBox="0 0 11 13"><path d="M.5.5h7l3 3v9H.5zM3 6h5M3 8h5M3 10h5" fill="none" stroke="#aaa"/></svg><span>Where can I find some quizes related to Norwegian Language?</span></div>
  <div class="list-item" style="top:534px"><svg width="11" height="13" viewBox="0 0 11 13"><path d="M.5.5h7l3 3v9H.5zM3 6h5M3 8h5M3 10h5" fill="none" stroke="#aaa"/></svg><span>What is the list of related organizations?</span></div>
  <div class="list-item" style="top:575px"><svg width="11" height="13" viewBox="0 0 11 13"><path d="M.5.5h7l3 3v9H.5zM3 6h5M3 8h5M3 10h5" fill="none" stroke="#aaa"/></svg><span>What this website can give me and what it can't?</span></div>
  <div class="list-item" style="top:616px"><svg width="11" height="13" viewBox="0 0 11 13"><path d="M.5.5h7l3 3v9H.5zM3 6h5M3 8h5M3 10h5" fill="none" stroke="#aaa"/></svg><span>Best places to find Norwegian Dictionary.</span></div>
  <div class="abs" style="left:706px;top:670px;font-size:13px;color:#888">»&nbsp;&nbsp; more</div>
</main>

<aside class="sidebar" style="top:804px;height:696px">
  <div class="brand">Lumadio Notes</div>
  <div class="abs" style="left:6px;top:107px;width:354px;height:42px;background:var(--teal);color:#fff;font-weight:700;font-size:14px;display:flex;align-items:center;justify-content:center;gap:6px"><svg width="16" height="12" viewBox="0 0 16 12"><path d="M1 1h5l2 2h6v2H4L1 11zM4 6h12l-3 6H1z" fill="#fff"/></svg>Categories</div>
  <div class="abs" style="left:6px;top:156px;width:350px;height:258px;border:1px solid var(--line)"></div>
  <div class="abs" style="left:15px;top:166px;width:331px;height:53px;background:#f3f3f3;border:1px solid #ccc;box-shadow:0 1px 2px rgba(0,0,0,.15);display:flex;align-items:center;gap:14px;padding-left:20px;font-size:19px;font-weight:700">
    <svg width="16" height="22" viewBox="0 0 16 22"><path d="M8 1a7 7 0 0 0-4 12.5V16h8v-2.5A7 7 0 0 0 8 1zM5 18h6M6 21h4" fill="none" stroke="#222" stroke-width="1.6"/></svg>Paragraph Titles</div>
  <div class="step" style="top:233px">Step1 : Downloading PressKit</div>
  <div class="step" style="top:276px">Step2 : Upload &amp; Extract</div>
  <div class="step" style="top:319px">Step3 : Run the Installer</div>
  <div class="step" style="top:362px">Comments</div>
  <div class="tags" style="top:429px"><span class="tag">cron</span><span class="tag">email</span><span class="tag">VPS</span></div>
</aside>

<main class="main" style="top:804px;height:696px;border-radius:20px 20px 0 0">
  <nav class="nav"><span>Home<span class="caret">▼</span></span><span>Articles</span><span>blog</span><span>F.A.Q</span></nav>
  <div class="contact">➤ Contact us</div>
  <div class="rule" style="top:103px"></div>
  <div class="search" style="top:125px">Search Blog ...</div>
  <section class="abs" style="left:15px;top:211px;width:765px;height:485px;background:#fff;box-shadow:0 1px 3px rgba(0,0,0,.2);overflow:hidden">
    <div class="abs" style="left:0;top:0;width:765px;height:78px;background:var(--grey-head);color:#fff;font-size:30px;font-weight:700;text-align:center;line-height:66px">Blog</div>
    <article class="abs" style="left:14px;top:93px;width:736px;height:338px;border:1px solid var(--line)">
      <div class="abs" style="left:14px;top:14px;width:706px;height:46px;background:var(--teal-soft);color:#fff;font-weight:700;font-size:15px;display:flex;align-items:center;padding-left:14px;gap:8px">➤ Official website is up now!</div>
      <div class="abs" role="img" aria-label="Photo of a Norwegian mountain cliff under a cloudy sky" style="left:29px;top:91px;width:150px;height:152px;background:linear-gradient(170deg,#c9d2d6 0%,#8b98a0 40%,#8a6a4a 70%,#4b3826 100%)"></div>
      <p class="abs" style="left:192px;top:91px;width:515px;font-size:15px;line-height:27px;color:#666">Several weeks ago our management team decided to start a new website for company, software utility Cron is a time-based job scheduler in Unix-like computer operating systems. People who set up and maintain software environments use cron to schedule jobs (commands or shell scripts) to run periodically at fixed times, dates, or .... <span style="display:inline-block;border:1px solid var(--teal);border-radius:14px;color:var(--teal);font-size:12px;font-weight:700;padding:2px 18px;line-height:20px">more</span></p>
      <div class="meta" style="left:14px;width:258px">▦ Publish date : <b style="color:#666">2017/11/20</b></div>
      <div class="meta" style="left:271px;width:237px">▭ Category : <b style="color:#666">Change Log</b></div>
      <div class="meta" style="left:507px;width:213px">⚇ Author : <b style="color:#666">username</b></div>
    </article>
    <article class="abs" style="left:14px;top:445px;width:736px;height:60px;border:1px solid var(--line)">
      <div class="abs" style="left:14px;top:14px;width:706px;height:46px;background:var(--teal-soft);color:#fff;font-weight:700;font-size:15px;display:flex;align-items:center;padding-left:14px;gap:8px">➤ Official website is up now!</div>
    </article>
  </section>
</main>

</div>
</div>
</body>
</html>
```